I need a cd cover for a new pop rock album called "Letters from the tin harbour"
The main color of the artwork shall obviously be orange. The artwork shouldn't be too "obvious", but it would be better something a bit abstract.
Please remember that it is a Music Cd Cover, so do not send business logo or advertisement images.

It's a pop rock album, so the target customers are young and adult people from 15-60 years old

• Orange as main colour
The Artist name is: Tomas Verhelst
The Title: Letters from the tin harbour
• Not too cheesy or dreamy images please. No simple sunset or sunrise pics

```html
<!DOCTYPE html>
<html lang="en">
<head>
<meta charset="utf-8">
<title>Letters from the tin harbour — Tomas Verhelst</title>
<link rel="stylesheet" href="https://fonts.googleapis.com/css2?family=Big+Shoulders+Display:wght@200;300&family=Roboto+Condensed:wght@700&display=swap">
<style>
  :root {
    --stage: #e9e9e9;
    --amber-light: #fbc02d;
    --amber: #f7a11a;
    --orange: #f2761a;
    --orange-deep: #e2541c;
    --ink-white: #ffffff;
    --box-text: #f08a1c;
    --artist-grey: #4a4a4a;
    --cloud-white: #fffaf2;
    --cloud-warm: #fde4bf;
  }
  * { margin: 0; padding: 0; box-sizing: border-box; }
  html, body {
    width: 1200px;
    height: 786px;
    overflow: hidden;
    background: var(--stage);
  }
  .canvas {
    position: relative;
    width: 1200px;
    height: 786px;
  }
  .cover {
    position: absolute;
    left: 260px;
    top: 53px;
    width: 680px;
    height: 680px;
    overflow: hidden;
    background:
      radial-gradient(ellipse 60% 45% at 22% 8%, rgba(255, 224, 110, 0.75), transparent 70%),
      radial-gradient(ellipse 70% 60% at 85% 95%, rgba(214, 66, 24, 0.55), transparent 70%),
      linear-gradient(160deg, var(--amber-light) 0%, var(--amber) 30%, var(--orange) 62%, var(--orange-deep) 100%);
  }
  .cloud-art {
    position: absolute;
    border-radius: 50%;
    filter: blur(10px);
  }
  .cloud-art--small {
    left: -10px;
    top: 228px;
    width: 250px;
    height: 120px;
    background: radial-gradient(ellipse at 50% 55%, var(--cloud-warm) 0%, rgba(253, 228, 191, 0.85) 45%, rgba(253, 228, 191, 0) 72%);
  }
  .cloud-art--large {
    left: 40px;
    top: 355px;
    width: 610px;
    height: 270px;
    background: radial-gradient(ellipse at 52% 50%, var(--cloud-white) 0%, rgba(255, 246, 232, 0.92) 40%, rgba(255, 240, 220, 0) 72%);
  }
  .title {
    position: absolute;
    left: 0;
    top: 18px;
    width: 100%;
    text-align: center;
    color: var(--ink-white);
    text-transform: uppercase;
  }
  .title__line {
    display: block;
    font-family: "Big Shoulders Display", "Oswald", sans-serif;
    font-weight: 200;
    font-size: 96px;
    line-height: 0.9;
    letter-spacing: 2px;
  }
  .title__boxed {
    display: inline-block;
    margin: 10px 0 6px;
    padding: 2px 12px 0;
    background: var(--ink-white);
    color: var(--box-text);
    font-family: "Roboto Condensed", "Arial Narrow", sans-serif;
    font-weight: 700;
    font-size: 34px;
    line-height: 36px;
    letter-spacing: 0.5px;
  }
  .artist {
    position: absolute;
    left: 0;
    top: 462px;
    width: 100%;
    text-align: center;
    font-family: "Roboto Condensed", "Arial Narrow", sans-serif;
    font-weight: 700;
    font-size: 26px;
    color: var(--artist-grey);
    text-shadow: 1px 2px 3px rgba(0, 0, 0, 0.3);
  }
</style>
</head>
<body>
  <main class="canvas">
    <section class="cover">
      <div class="cloud-art cloud-art--small" role="img" aria-label="Small drifting white cloud"></div>
      <div class="cloud-art cloud-art--large" role="img" aria-label="Large billowing white cloud with scattered particles"></div>
      <h1 class="title">
        <span class="title__line">Letters from</span>
        <span class="title__boxed">The tin</span>
        <span class="title__line">Harbour</span>
      </h1>
      <p class="artist">Tomas Verhelst</p>
    </section>
  </main>
</body>
</html>
```